Consulting company, design, Interior design in commercial real estate (Tertiai sector *

Company name: VORANDEL: from the Greek Evexia well-being, was born from a desire to combine well-being and work. By the choice of design, materials, design and furniture, everything is thought from this perspective

Logo: Essay with Möbius Ribbon and / or with the infinite acronym / and or triangle ...
Sentences to write:
"The exclusive partner for your development projects"
"Consulting - Design - Construction"
"We manage EVERYTHING for you"

On the back: Photo (attached; if photo is not clear, another photo can be provided) with company name and "VORANDEL, Excellence and reliability"
My name / First name: provided later (double name), Manager
Address: supplied later
Tel: supplied later
Website: www. vorandel.com
Colors: Black, gold and white. Other admissible colors
See attached files

Real estate business

Nom de l'entreprise : VORANDEL : du grec Evexia bien être, est né d'une volonté de faire rimer bien être et travail. Par le choix de la conception, des matériaux, du design et du mobilier, tout est pensé dans cette optique

Logo : Essai avec Ruban de Möbius et /ou avec le sigle infini / et ou triangle...
Phrases à inscrire :
"Le partenaire exclusif de vos projets d'aménagement"
"Conseil - Conception - Construction"
"Nous gérons TOUT pour vous"

Au verso : Photo (ci-jointe ; si photo pas nette, une autre photo peut être fournie) avec nom de l'entreprise et Mention "VORANDEL, Excellence et fiabilité"
Mon nom / Prénom : fourni ultérieurement (prénom double), Gérant
Adresse : fourni ultérieurement
Tél : fourni ultérieurement
Site Web : www. vorandel.com
Couleurs : Noir, doré et blanc. Autre couleurs recevables
Voir fichiers ci-joint

• My project must be simple, clear, neat and design.
The business card must catch the customer

```html
<!DOCTYPE html>
<html lang="en">
<head>
<meta charset="utf-8">
<title>Vorandel — Business Cards</title>
<link href="https://fonts.googleapis.com/css2?family=Arimo:wght@400;700&display=swap" rel="stylesheet">
<style>
  :root {
    --stage: #2a2a2a;
    --card-black: #000000;
    --card-white: #ffffff;
    --gold: #f3a51f;
    --grey: #8c8c8c;
    --ink: #111111;
    --text-light: #ffffff;
  }
  * { box-sizing: border-box; margin: 0; padding: 0; }
  html, body {
    width: 1200px; height: 1015px; overflow: hidden;
    background: var(--stage);
    font-family: "Arimo", Arial, sans-serif;
  }
  .canvas { position: relative; width: 1200px; height: 1015px; }

  .card {
    position: absolute; width: 720px; height: 412px;
    background: var(--card-black); overflow: hidden;
    box-shadow: 0 18px 40px rgba(0,0,0,.55);
  }
  .card--front { left: 90px; top: 70px; }
  .card--back  { left: 390px; top: 533px; }

  .card__shape { position: absolute; inset: 0; width: 720px; height: 412px; }

  /* Front */
  .brand {
    position: absolute; left: 430px; top: 105px; width: 270px;
    text-align: center; color: var(--ink);
  }
  .brand__name {
    font-weight: 700; font-size: 42px; letter-spacing: 2px; line-height: 1;
  }
  .brand__tagline {
    margin-top: 10px; font-size: 10.5px; letter-spacing: 2px;
    color: var(--grey); text-transform: uppercase; font-weight: 700;
    white-space: nowrap;
  }
  .services {
    position: absolute; left: 44px; top: 170px; width: 320px;
    list-style: none; color: var(--text-light);
  }
  .services li {
    position: relative; padding-left: 30px; margin-bottom: 20px;
    font-size: 19px; line-height: 1.15;
  }
  .services li::before {
    content: ""; position: absolute; left: 0; top: 8px;
    width: 11px; height: 11px; border-radius: 50%; background: var(--gold);
  }

  /* Back */
  .contact {
    position: absolute; left: 50px; top: 150px; width: 340px;
    color: var(--text-light);
  }
  .contact__name {
    color: var(--gold); font-weight: 700; font-size: 26px;
    letter-spacing: 1px; line-height: 1; white-space: nowrap;
  }
  .contact__role { font-size: 20px; margin-top: 4px; }
  .contact__address { font-size: 20px; line-height: 1.2; margin-top: 20px; font-style: normal; }
  .contact__lines { list-style: none; margin-top: 20px; }
  .contact__lines li {
    display: flex; align-items: center; gap: 10px;
    font-size: 19px; line-height: 1.35;
  }
  .contact__icon { width: 18px; height: 18px; flex: none; }

  .portrait {
    position: absolute; left: 498px; top: 45px;
    width: 208px; height: 208px; border-radius: 50%;
    background: linear-gradient(160deg, #e4e2dc 0%, #d9d6cf 45%, #c7b2a4 60%, #2b3447 100%);
  }
</style>
</head>
<body>
<main class="canvas">

  <section class="card card--front">
    <svg class="card__shape" viewBox="0 0 720 412" aria-hidden="true">
      <circle cx="600" cy="130" r="230" fill="var(--card-white)"/>
      <circle cx="608" cy="126" r="222" fill="var(--gold)"/>
      <circle cx="612" cy="124" r="218" fill="var(--card-white)"/>
    </svg>
    <div class="brand">
      <div class="brand__name">VORANDEL</div>
      <div class="brand__tagline">Excellence and reliability</div>
    </div>
    <ul class="services">
      <li>The exclusive partner for your<br>development projects</li>
      <li>Consulting - Design<br>Construction</li>
      <li>We manage<br>EVERYTHING for you</li>
    </ul>
  </section>

  <section class="card card--back">
    <svg class="card__shape" viewBox="0 0 720 412" aria-hidden="true">
      <circle cx="640" cy="150" r="230" fill="var(--card-white)"/>
      <circle cx="648" cy="146" r="222" fill="var(--gold)"/>
      <circle cx="652" cy="144" r="218" fill="var(--card-white)"/>
    </svg>
    <div class="portrait" role="img" aria-label="Portrait photo of the managing director"></div>

    <div class="contact">
      <div class="contact__name">JULIEN MARCELLAN</div>
      <div class="contact__role">Managing Director</div>
      <address class="contact__address">18 , Rue des Tilleuls<br>Lyon, France 69002</address>
      <ul class="contact__lines">
        <li>
          <svg class="contact__icon" viewBox="0 0 24 24" aria-hidden="true"><path fill="var(--gold)" d="M6.6 10.8a15 15 0 0 0 6.6 6.6l2.2-2.2a1 1 0 0 1 1-.25 11.4 11.4 0 0 0 3.6.57 1 1 0 0 1 1 1V20a1 1 0 0 1-1 1A17 17 0 0 1 3 4a1 1 0 0 1 1-1h3.5a1 1 0 0 1 1 1c0 1.25.2 2.450.57 3.57a1 1 0 0 1-.25 1z"/></svg>
          044-987 210 345
        </li>
        <li>
          <svg class="contact__icon" viewBox="0 0 24 24" aria-hidden="true"><rect x="2" y="5" width="20" height="14" fill="var(--gold)"/><path d="M2 5l10 8 10-8" fill="none" stroke="var(--card-black)" stroke-width="1.6"/></svg>
          contact@vorandel.com
        </li>
        <li>
          <svg class="contact__icon" viewBox="0 0 24 24" aria-hidden="true"><g fill="none" stroke="var(--gold)" stroke-width="2"><circle cx="12" cy="12" r="9.5"/><ellipse cx="12" cy="12" rx="4" ry="9.5"/><path d="M2.5 12h19M4 7h16M4 17h16"/></g></svg>
          www.vorandel.com
        </li>
      </ul>
    </div>
  </section>

</main>
</body>
</html>
```